Poster for a 100 y.o. Tennis Tournament

I would like a poster designed to promote our tennis tournament but I'd like to avoid some of the clichés like the shadow of a player serving. Just well styled text would be fine but some clever imagery would be a bonus.
Highlighting the fact our tournament has been running for over 100 years would be nice so a retro design would work. But that doesn't mean a modern design, for example a minimalist approach utilising the lines of a tennis court, wouldn't work.
Updates

Our tennis committee is now in the process of short listing and will provide an update within 48 hours.

Industry/Entity Type

Court

Requirements
Must have
• The poster must contain the following text at a minimum:
"Brimley Tennis Tournament"/"Since 1908"
"9 March - 11 March, 2013" or "9-11 March, 2013", etc
"www.brimleytennis.com.au"

The poster must be reproducible in colour and black & white, or at least have an alternate for black & white.

The poster must be usable in both A3 and A4 sizes.
Nice to have
• The poster should contain the following text:
"Championship"
"Handicap"
"Seniors"
"Juniors"
Each above may be optionally succeeded by "Singles & Doubles", e.g. "Championship Singles & Doubles". It would actually be clearer if this additional text was used but would be repetitive, so alternate text "Singles & Doubles in all categories" might also be used. Alternatives for variety (with the first word the focus): "Championship Singles & Doubles", "Handicap Singles & Doubles", "Seniors 35+ & 50+", "Juniors 18&U, 14&U"

Ideally the poster will provision room for four to eight sponsors logos, preferably at the bottom, but failure to do this is not a show stopper.

The following text may also be used:
"Entries close February 24"
"Marnock Plate Weekend"

Attached is a photo of one of the old trophies. Utilisation of the curved style of the "Brimley Tennis Tournament" text would fit in with the history if the tournament.

The ability to reuse elements of the poster in a single page website used to promote the tournament would be an advantage (as it will provide consistency).

If you could have an image of a tennis ball that conveys the same energy as the clock/tyre image in the attached "Beyond the Hourglass" poster, that would be cool. Or using split imagery of a wooden racquet and a modern racquet, but with some energy, would also be good. These are just ideas though and by no means essential.

I've also attached a photo of a t-shirt with a poster layout I thought looked good.

Some additional text that can be used:
"Brand new courts"
"Corbin Field, Loxley Tce, Brimley"
"Phone 0427 318 642"
"Prizes and Trophies"

```html
<!DOCTYPE html>
<html lang="en">
<head>
<meta charset="utf-8">
<title>Brimley Tennis Tournament</title>
<link rel="stylesheet" href="https://fonts.googleapis.com/css2?family=Roboto+Slab:wght@400&display=swap">
<style>
  :root {
    --page: #ffffff;
    --court: #9cc43a;
    --court-edge: #7ea62a;
    --court-line: #b4d664;
    --accent: #d7df00;
    --ball-seam: #9cc43a;
    --ink: #ffffff;
  }
  html, body {
    margin: 0;
    padding: 0;
    width: 1200px;
    height: 1200px;
    overflow: hidden;
    background: var(--page);
  }
  .canvas {
    display: block;
    width: 1200px;
    height: 1200px;
  }
  .poster-text {
    font-family: "Roboto Slab", Georgia, serif;
    font-weight: 400;
    fill: var(--ink);
  }
  .court-line { stroke: var(--court-line); stroke-width: 7; fill: none; opacity: 0.85; }
  .rule { fill: var(--accent); }
  .ball { fill: var(--accent); }
  .ball-seam { stroke: var(--ball-seam); stroke-width: 2; fill: none; }
</style>
</head>
<body>
<svg class="canvas" viewBox="0 0 1000 1000" xmlns="http://www.w3.org/2000/svg" aria-label="Brimley Tennis Tournament poster">
  <defs>
    <radialGradient id="court-fill" cx="50%" cy="45%" r="75%">
      <stop offset="0%" stop-color="var(--court)"/>
      <stop offset="75%" stop-color="var(--court)"/>
      <stop offset="100%" stop-color="var(--court-edge)"/>
    </radialGradient>
    <filter id="poster-shadow" x="-10%" y="-10%" width="120%" height="120%">
      <feDropShadow dx="0" dy="2" stdDeviation="4" flood-opacity="0.3"/>
    </filter>
  </defs>

  <!-- poster sheet -->
  <rect class="poster" x="193" y="65" width="617" height="867" fill="url(#court-fill)" filter="url(#poster-shadow)"/>

  <!-- court markings -->
  <g class="court">
    <rect class="court-line" x="218" y="88" width="567" height="822"/>
    <line class="court-line" x1="238" y1="88" x2="238" y2="910"/>
    <line class="court-line" x1="765" y1="88" x2="765" y2="910"/>
    <line class="court-line" x1="238" y1="290" x2="765" y2="290"/>
    <line class="court-line" x1="218" y1="500" x2="785" y2="500"/>
    <line class="court-line" x1="238" y1="712" x2="765" y2="712"/>
    <line class="court-line" x1="502" y1="290" x2="502" y2="712"/>
  </g>

  <!-- title -->
  <text class="poster-text title" x="260" y="208" font-size="112" textLength="485" lengthAdjust="spacingAndGlyphs">BRIMLEY</text>
  <text class="poster-text title" x="260" y="312" font-size="112" textLength="485" lengthAdjust="spacingAndGlyphs">TENNIS</text>
  <text class="poster-text subtitle" x="262" y="390" font-size="76" textLength="483" lengthAdjust="spacingAndGlyphs">TOURNAMENT</text>

  <!-- heritage row with balls -->
  <g class="balls">
    <g transform="translate(280 427)"><circle class="ball" r="16"/><path class="ball-seam" d="M-9,-13 C-2,-5 -2,5 -9,13 M9,-13 C2,-5 2,5 9,13"/></g>
    <g transform="translate(320 427)"><circle class="ball" r="16"/><path class="ball-seam" d="M-9,-13 C-2,-5 -2,5 -9,13 M9,-13 C2,-5 2,5 9,13"/></g>
    <g transform="translate(360 427)"><circle class="ball" r="16"/><path class="ball-seam" d="M-9,-13 C-2,-5 -2,5 -9,13 M9,-13 C2,-5 2,5 9,13"/></g>
    <g transform="translate(645 427)"><circle class="ball" r="16"/><path class="ball-seam" d="M-9,-13 C-2,-5 -2,5 -9,13 M9,-13 C2,-5 2,5 9,13"/></g>
    <g transform="translate(685 427)"><circle class="ball" r="16"/><path class="ball-seam" d="M-9,-13 C-2,-5 -2,5 -9,13 M9,-13 C2,-5 2,5 9,13"/></g>
    <g transform="translate(725 427)"><circle class="ball" r="16"/><path class="ball-seam" d="M-9,-13 C-2,-5 -2,5 -9,13 M9,-13 C2,-5 2,5 9,13"/></g>
  </g>
  <text class="poster-text since" x="397" y="440" font-size="36" textLength="211" lengthAdjust="spacingAndGlyphs">SINCE 1908</text>

  <rect class="rule" x="260" y="453" width="485" height="6"/>

  <text class="poster-text dates" x="260" y="515" font-size="56" textLength="485" lengthAdjust="spacingAndGlyphs">9 – 11 MARCH 2013</text>

  <rect class="rule" x="260" y="537" width="485" height="6"/>

  <!-- events grid -->
  <rect class="rule" x="503" y="543" width="5" height="79"/>
  <text class="poster-text event" x="260" y="582" font-size="33" textLength="230" lengthAdjust="spacingAndGlyphs">CHAMPIONSHIP</text>
  <text class="poster-text event-note" x="260" y="602" font-size="18" textLength="232" lengthAdjust="spacingAndGlyphs">(SINGLES &amp; DOUBLES)</text>
  <text class="poster-text event" x="516" y="582" font-size="33" textLength="229" lengthAdjust="spacingAndGlyphs">HANDICAP</text>
  <text class="poster-text event-note" x="516" y="602" font-size="18" textLength="229" lengthAdjust="spacingAndGlyphs">(SINGLES &amp; DOUBLES)</text>

  <rect class="rule" x="260" y="620" width="485" height="6"/>

  <rect class="rule" x="503" y="626" width="5" height="140"/>
  <text class="poster-text division" x="260" y="692" font-size="52" textLength="230" lengthAdjust="spacingAndGlyphs">SENIORS</text>
  <text class="poster-text division" x="260" y="745" font-size="52" textLength="230" lengthAdjust="spacingAndGlyphs">35+ &amp; 50+</text>
  <text class="poster-text division" x="516" y="692" font-size="52" textLength="229" lengthAdjust="spacingAndGlyphs">JUNIORS</text>
  <text class="poster-text division" x="516" y="745" font-size="52" textLength="229" lengthAdjust="spacingAndGlyphs">U14 &amp; U18</text>

  <rect class="rule" x="260" y="766" width="485" height="6"/>

  <text class="poster-text web" x="260" y="815" font-size="38" textLength="485" lengthAdjust="spacingAndGlyphs">www.brimleytennis.com.au</text>

  <rect class="rule sponsor-band" x="260" y="833" width="485" height="42"/>
</svg>
</body>
</html>
```